HK-Steuerberatung WordPress Site fully implemented (tax advisor)

Hello!
I need a little Wordpress Site for my newly founded Tax-Advisor Company.
I am a one-man Office advising in the area of Crypto-Currency.
PLEASE only provide a Design, if you can also Implement a WP-Site afterwards on an existing Webspace.

Please find the Content and Website-Description in the attached Document

Language for the Website is German (for now)

Target Market(s)

Tax-Advisory (specialized in Crypto Currency)

Coding

Coded - Design and coding required

Number of Pages Required

5+ page

Font styles to use
Sans Serif

Requirements
Must have
• Wordpress Implementation afterwards - Details according to attached Project Information Document

```html
<!DOCTYPE html>
<html lang="de">
<head>
<meta charset="utf-8">
<title>HK-Steuerberatung</title>
<link href="https://fonts.googleapis.com/css2?family=Montserrat:wght@400;500;600;700&display=swap" rel="stylesheet">
<style>
:root{
  --navy:#1b2c4f;
  --ink:#243a63;
  --muted:#9a9a9a;
  --grey-band:#f2f2f2;
  --button:#a4a4a4;
  --white:#ffffff;
  --text-dark:#2b2b2b;
  --icon-tone-a:#dfe4ee;
  --icon-tone-b:#c8d1e2;
}
*{margin:0;padding:0;box-sizing:border-box}
html,body{width:996px;height:1200px;overflow:hidden;background:var(--white);font-family:"Montserrat",Arial,sans-serif}
.page{position:relative;width:996px;height:1200px;overflow:hidden}
.hero-band{position:absolute;left:0;top:0;width:996px;height:514px;
  background:radial-gradient(ellipse at 15% 20%,#2d4a78 0%,transparent 45%),
             radial-gradient(ellipse at 80% 55%,#2a4a80 0%,transparent 50%),
             linear-gradient(160deg,#1a2d52 0%,#1c325d 60%,#223f70 100%);
  clip-path:polygon(0 0,100% 0,100% 514px,0 411px)}
.brand{position:absolute;left:134px;top:48px;font-weight:700;font-size:16px;letter-spacing:.3px;color:var(--white)}
.main-nav{position:absolute;top:51px;left:0;font-size:11px;color:var(--white)}
.main-nav a{position:absolute;white-space:nowrap;color:inherit;text-decoration:none}
.main-nav .active{font-weight:700}
.hero-photo{position:absolute;left:134px;top:135px;width:360px;height:393px;border-radius:37px 0 0 6px;
  background:linear-gradient(135deg,#d9d4cc 0%,#b9c6d6 40%,#8a9fbd 60%,#7a5c44 100%)}
.hero-title{position:absolute;left:537px;top:192px;font-size:29px;line-height:37px;font-weight:700;color:var(--white)}
.hero-lead{position:absolute;left:539px;top:282px;font-size:11.6px;line-height:18.5px;color:var(--white)}
.hero-button{position:absolute;left:540px;top:336px;width:128px;height:38px;background:var(--button);border-radius:8px 0 0 0;
  color:var(--white);font-size:11.5px;line-height:38px;text-align:center}
.feature{position:absolute;top:605px;width:240px;text-align:center}
.feature-icon{margin:0 auto;height:70px;border-radius:14px;background:linear-gradient(90deg,var(--icon-tone-a),var(--icon-tone-b))}
.feature-text{margin-top:26px;font-size:13px;line-height:20.5px;font-weight:500;color:var(--ink);letter-spacing:.2px;white-space:nowrap}
.feature-text span{color:var(--muted)}
.footer-band{position:absolute;left:0;top:781px;width:996px;height:419px;background:var(--grey-band);
  clip-path:polygon(0 104px,100% 0,100% 100%,0 100%)}
.footer-brand{position:absolute;left:0;width:996px;top:926px;text-align:center;font-weight:700;font-size:16px;color:var(--navy)}
.footer-nav{position:absolute;top:998px;left:0;font-size:11px;color:var(--text-dark)}
.footer-nav a{position:absolute;white-space:nowrap;color:inherit;text-decoration:none}
.contact{position:absolute;top:1052px;font-size:11px;line-height:15px;color:var(--text-dark)}
.contact strong{display:block;font-weight:700}
.contact svg{position:absolute;left:-38px;top:1px}
.contact-divider{position:absolute;left:517px;top:1053px;width:1px;height:29px;background:var(--text-dark)}
.legal-bar{position:absolute;left:0;top:1157px;width:996px;height:43px;background:var(--navy);color:var(--white);
  font-size:10.5px;line-height:43px;text-align:center}
</style>
</head>
<body>
<div class="page">
  <div class="hero-band"></div>
  <div class="brand">HK STEUERBERATUNG</div>
  <nav class="main-nav">
    <a class="active" style="left:466px">Heim</a>
    <a style="left:531px">Leistungen</a>
    <a style="left:629px">Über Mich</a>
    <a style="left:721px">Kontakt</a>
    <a style="left:802px">Impressum</a>
  </nav>

  <div class="hero-photo" role="img" aria-label="Foto: Steuerberater arbeitet am Schreibtisch im hellen Büro"></div>
  <h1 class="hero-title">Willkommen Bei<br>HK-Steuerberatung!</h1>
  <p class="hero-lead">Ihrem Spezialisten Bei Allen Steuerlichen Themen<br>Rund Um Einkünfte &amp; Vermögen Aus Krypto-Assets.</p>
  <div class="hero-button">Dienste anzeigen</div>

  <div class="feature" style="left:132px">
    <div class="feature-icon" style="width:66px" role="img" aria-label="Illustration: Steuerdokument mit Ablehnungssymbol"></div>
    <p class="feature-text">Dann Mach Ich Eine Schweizer<br>Holding - Gesellschaft – <span>Dort</span><br><span>Zahlt Man Fast Keine Steuern</span></p>
  </div>

  <div class="feature" style="left:382px">
    <div class="feature-icon" style="width:134px" role="img" aria-label="Umrisskarte von Österreich mit Personensymbol"></div>
    <p class="feature-text">Dann Melde Ich Einfach<br>Meinen Hauptwohnsitz <span>In</span><br><span>Österreich Ab</span></p>
  </div>

  <div class="feature" style="left:629px">
    <div class="feature-icon" style="width:130px" role="img" aria-label="Umrisskarte von Singapur mit Währungssymbol"></div>
    <p class="feature-text">Dann Lass Ich Meine Kryptos<br>Auf Einer Börse In Singapur,<br><span>Dort Ist Das Steuerfrei</span></p>
  </div>

  <div class="footer-band"></div>
  <div class="footer-brand">HK STEUERBERATUNG</div>
  <nav class="footer-nav">
    <a style="left:293px">Heim</a>
    <a style="left:360px">Leistungen</a>
    <a style="left:461px">Über Mich</a>
    <a style="left:558px">Kontakt</a>
    <a style="left:642px">Impressum</a>
  </nav>

  <div class="contact" style="left:359px">
    <svg width="26" height="28" viewBox="0 0 26 28" fill="none" stroke="#243a63" stroke-width="1.4">
      <path d="M1 11 L13 3 L25 11 V27 H1 Z"/><path d="M1 11 L13 20 L25 11"/>
      <rect x="6" y="6" width="14" height="10" fill="#f2f2f2"/><line x1="9" y1="10" x2="17" y2="10"/><line x1="9" y1="13" x2="17" y2="13"/>
    </svg>
    <strong>Email</strong>office@hk-steuer.example
  </div>
  <div class="contact-divider"></div>
  <div class="contact" style="left:583px">
    <svg width="28" height="28" viewBox="0 0 28 28" fill="none" stroke="#243a63" stroke-width="1.4">
      <path d="M5 4 L9 3 L12 9 L9 11 C10 15 13 18 17 19 L19 16 L25 19 L24 23 C20 27 2 18 5 4 Z"/>
      <path d="M16 8 A5 5 0 0 1 20 12"/><path d="M16 4 A9 9 0 0 1 24 12"/>
    </svg>
    <strong>Telefon</strong>+43 512 000 417
  </div>

  <footer class="legal-bar">© 2022 HK STEUERBERATUNG. All Rights Reserved.</footer>
</div>
</body>
</html>
```